Menu redesign of existing iPhone app Glimra

We need a design upgrade for a footer menu of an iPhone app. We need to incorporate a new button for competitions/missions and it should be extremely modern and clean. The central button to create a Glimra cannot be too different as our current users are familiar with its usage.

I have attached screenshots of the curent newsfeed and menu.

Target Market(s)

Photography lovers/ design lovers

Font styles to use
Sans Serif

Requirements
Must have
• Glimra Button,
• Home button,
• My Profile button,
• Find friends button,
• Notifications button,
• Settings button,
• Missions/Competition Button
Nice to have
• Similar Glimra button as existing on the app

```html
<!DOCTYPE html>
<html lang="en">
<head>
<meta charset="utf-8">
<title>Glimra footer menu</title>
<link rel="stylesheet" href="https://fonts.googleapis.com/css2?family=Raleway:wght@300;400;500&family=Inter:wght@400;500&display=swap">
<style>
  :root{
    --bg:#ffffff;
    --pink:#e0245e;
    --bar:#f3f3f3;
    --tile:#f7f7f7;
    --line:#d9d9d9;
    --ink:#2c2c2c;
    --ink-soft:#6a6a6a;
    --status:#111111;
  }
  *{box-sizing:border-box;margin:0;padding:0}
  html,body{width:1200px;height:1200px;overflow:hidden;background:var(--bg)}
  body{position:relative;font-family:"Raleway",sans-serif;color:var(--ink)}
  .screen{
    position:absolute;top:108px;width:480px;height:855px;
    transform:scale(1.15);transform-origin:0 0;
    overflow:hidden;background:#dfe6ee;
    box-shadow:0 0 0 1px #e6e6e6;
  }
  .screen--menu-open{left:24px}
  .screen--footer{left:624px}

  .status-bar{position:absolute;left:0;top:0;width:480px;height:36px;background:#fff;
    font-family:"Inter",sans-serif;font-size:17px;color:var(--status)}
  .status-bar .signal{position:absolute;left:10px;top:11px}
  .status-bar .time{position:absolute;left:0;right:0;top:8px;text-align:center;font-weight:400}
  .status-bar .battery{position:absolute;right:8px;top:8px;display:flex;align-items:center;gap:6px}

  .cover-photo{position:absolute;left:0;top:36px;width:480px;height:132px;
    background:linear-gradient(180deg,#a98f1c 0%,#c9a520 40%,#b6901a 75%,#d2b02a 100%)}

  .post-header{position:absolute;z-index:2;left:0;top:168px;width:480px;height:77px;background:var(--bar)}
  .post-header .avatar{position:absolute;left:74px;top:13px;width:52px;height:52px;border-radius:50%;
    background:radial-gradient(circle at 50% 45%,#c98a6a 0%,#8a4a32 70%,#5a2c1e 100%)}
  .post-header .title{position:absolute;left:0;right:0;top:14px;text-align:center;font-size:22px;font-weight:300;letter-spacing:.2px}
  .post-header .age{position:absolute;left:0;right:0;top:44px;text-align:center;font-size:13px;font-weight:400;color:var(--ink-soft)}
  .post-header .stats{position:absolute;left:394px;top:15px;font-family:"Inter",sans-serif;font-size:12px;color:var(--ink-soft)}
  .post-header .stat{display:flex;align-items:center;gap:5px;height:23px}
  .post-header .pointer{position:absolute;left:228px;bottom:-12px;width:0;height:0;
    border-left:12px solid transparent;border-right:12px solid transparent;border-top:12px solid var(--bar)}

  .post-photo{position:absolute;left:0;top:245px;width:480px;height:610px;
    background:
      radial-gradient(ellipse at 75% 55%,#ffffff 0%,#eef1f5 30%,rgba(238,241,245,0) 60%),
      radial-gradient(ellipse at 80% 95%,#f7f8fa 0%,rgba(247,248,250,0) 55%),
      linear-gradient(160deg,#c9d3de 0%,#8e9fb4 45%,#b7c3d2 75%,#e9edf2 100%)}

  .action-grid{position:absolute;left:4px;top:733px;width:472px;display:grid;
    grid-template-columns:232px 234px;grid-template-rows:57px 55px;column-gap:6px;row-gap:5px}
  .action{display:flex;align-items:center;gap:14px;padding-left:12px;background:var(--tile);
    font-size:20px;font-weight:400;color:var(--ink);box-shadow:0 1px 2px rgba(0,0,0,.12);white-space:nowrap}
  .action--cancel{background:var(--pink);color:#fff}

  .icon-bar{position:absolute;left:6px;top:733px;width:468px;height:57px;background:var(--tile);
    box-shadow:0 1px 2px rgba(0,0,0,.12)}
  .icon-bar .menu-icon{position:absolute;top:14px}
  .icon-bar .divider{position:absolute;top:10px;width:1px;height:37px;background:var(--line)}
  .nav-bar{position:absolute;left:6px;top:795px;width:468px;height:55px;background:var(--pink)}
  .nav-bar .nav-icon{position:absolute;top:13px}
  .nav-bar .divider{position:absolute;left:234px;top:6px;width:1px;height:43px;background:rgba(255,255,255,.45)}
  .capture-button{position:absolute;left:186px;top:679px;width:108px;height:108px;border-radius:50%;
    background:radial-gradient(circle at 50% 40%,#ffffff 0%,#f1f1f1 70%,#e4e4e4 100%);
    border:9px solid var(--pink);box-shadow:0 3px 6px rgba(0,0,0,.2)}
  .capture-button .dot{position:absolute;left:35px;top:35px;width:20px;height:20px;border-radius:50%;background:var(--pink)}
</style>
</head>
<body>

<!-- Screen with upload actions -->
<section class="screen screen--menu-open">
  <div class="status-bar">
    <svg class="signal" width="70" height="14" viewBox="0 0 70 14" fill="#111"><circle cx="5" cy="7" r="4.5"/><circle cx="16" cy="7" r="4.5"/><circle cx="27" cy="7" r="4.5"/><circle cx="38" cy="7" r="4.5"/><circle cx="49" cy="7" r="4.5"/><path d="M62 12 l-2-2.2 a3 3 0 0 1 4 0z M62 5 a7 7 0 0 1 6 2.4 l-1.4 1.4 a5 5 0 0 0-9.2 0 l-1.4-1.4 A7 7 0 0 1 62 5z" transform="translate(0,-1)"/></svg>
    <div class="time">9:41 AM</div>
    <div class="battery">100%<svg width="38" height="16" viewBox="0 0 38 16"><rect x="1" y="1" width="33" height="14" rx="2" fill="none" stroke="#111" stroke-width="1.5"/><rect x="3" y="3" width="29" height="10" fill="#111"/><rect x="35" y="5" width="2" height="6" fill="#111"/></svg></div>
  </div>
  <div class="cover-photo" role="img" aria-label="Cover photo of a golden grass meadow"></div>
  <div class="post-header">
    <div class="avatar" role="img" aria-label="Profile photo of the poster"></div>
    <div class="title">Irva Staff Pick</div>
    <div class="age">15 ours ago</div>
    <div class="stats">
      <div class="stat"><svg width="20" height="18" viewBox="0 0 20 18" fill="none" stroke="#777" stroke-width="1.2"><path d="M10 2c4.4 0 8 2.6 8 6s-3.6 6-8 6c-1 0-2-.1-2.8-.4L3 16l1.2-3.4C2.8 11.5 2 9.9 2 8c0-3.4 3.6-6 8-6z"/><circle cx="7" cy="8" r=".6" fill="#777"/><circle cx="10" cy="8" r=".6" fill="#777"/><circle cx="13" cy="8" r=".6" fill="#777"/></svg>32</div>
      <div class="stat"><svg width="20" height="18" viewBox="0 0 20 18" fill="none" stroke="#777" stroke-width="1.2"><path d="M10 1.5l2.5 5.2 5.6.7-4.1 3.9 1 5.6L10 14.2 5 16.9l1-5.6L1.9 7.4l5.6-.7z"/></svg>158</div>
    </div>
    <div class="pointer"></div>
  </div>
  <div class="post-photo" role="img" aria-label="Photo of frost-covered branches in snow"></div>

  <div class="action-grid">
    <div class="action"><svg width="26" height="26" viewBox="0 0 26 26" fill="none" stroke="#8a8a8a" stroke-width="1.3" stroke-dasharray="3 3"><rect x="1" y="1" width="24" height="24"/></svg>Select Glimra Pic</div>
    <div class="action"><svg width="26" height="26" viewBox="0 0 26 26" fill="none" stroke="#8a8a8a" stroke-width="1.3"><rect x="1" y="1" width="24" height="24" stroke-dasharray="3 3"/><path d="M10 8l7 5-7 5z"/></svg>Select Video</div>
    <div class="action action--cancel"><svg width="24" height="24" viewBox="0 0 24 24" stroke="#fff" stroke-width="1.5"><path d="M3 3l18 18M21 3L3 21"/></svg>Cancel</div>
    <div class="action"><svg width="26" height="26" viewBox="0 0 26 26" fill="none" stroke="#777" stroke-width="1.3"><circle cx="13" cy="13" r="11.5"/><path d="M10.5 8.5l6.5 4.5-6.5 4.5z"/></svg>Create Video</div>
  </div>
</section>

<!-- Screen with redesigned footer -->
<section class="screen screen--footer">
  <div class="status-bar">
    <svg class="signal" width="70" height="14" viewBox="0 0 70 14" fill="#111"><circle cx="5" cy="7" r="4.5"/><circle cx="16" cy="7" r="4.5"/><circle cx="27" cy="7" r="4.5"/><circle cx="38" cy="7" r="4.5"/><circle cx="49" cy="7" r="4.5"/><path d="M62 12 l-2-2.2 a3 3 0 0 1 4 0z M62 5 a7 7 0 0 1 6 2.4 l-1.4 1.4 a5 5 0 0 0-9.2 0 l-1.4-1.4 A7 7 0 0 1 62 5z" transform="translate(0,-1)"/></svg>
    <div class="time">9:41 AM</div>
    <div class="battery">100%<svg width="38" height="16" viewBox="0 0 38 16"><rect x="1" y="1" width="33" height="14" rx="2" fill="none" stroke="#111" stroke-width="1.5"/><rect x="3" y="3" width="29" height="10" fill="#111"/><rect x="35" y="5" width="2" height="6" fill="#111"/></svg></div>
  </div>
  <div class="cover-photo" role="img" aria-label="Cover photo of a golden grass meadow"></div>
  <div class="post-header">
    <div class="avatar" role="img" aria-label="Profile photo of the poster"></div>
    <div class="title">Irva Staff Pick</div>
    <div class="age">15 ours ago</div>
    <div class="stats">
      <div class="stat"><svg width="20" height="18" viewBox="0 0 20 18" fill="none" stroke="#777" stroke-width="1.2"><path d="M10 2c4.4 0 8 2.6 8 6s-3.6 6-8 6c-1 0-2-.1-2.8-.4L3 16l1.2-3.4C2.8 11.5 2 9.9 2 8c0-3.4 3.6-6 8-6z"/><circle cx="7" cy="8" r=".6" fill="#777"/><circle cx="10" cy="8" r=".6" fill="#777"/><circle cx="13" cy="8" r=".6" fill="#777"/></svg>32</div>
      <div class="stat"><svg width="20" height="18" viewBox="0 0 20 18" fill="none" stroke="#777" stroke-width="1.2"><path d="M10 1.5l2.5 5.2 5.6.7-4.1 3.9 1 5.6L10 14.2 5 16.9l1-5.6L1.9 7.4l5.6-.7z"/></svg>158</div>
    </div>
    <div class="pointer"></div>
  </div>
  <div class="post-photo" role="img" aria-label="Photo of frost-covered branches in snow"></div>

  <nav class="icon-bar" aria-label="Main menu">
    <svg class="menu-icon" style="left:23px" width="32" height="32" viewBox="0 0 32 32" fill="none" stroke="#8a8a8a" stroke-width="1.4" aria-label="My profile"><circle cx="16" cy="16" r="14.5"/><circle cx="16" cy="12.5" r="5"/><path d="M7 25.5c2-4.5 5.3-6.5 9-6.5s7 2 9 6.5"/></svg>
    <div class="divider" style="left:80px"></div>
    <svg class="menu-icon" style="left:108px" width="42" height="30" viewBox="0 0 42 30" fill="none" stroke="#8a8a8a" stroke-width="1.4" aria-label="Find friends"><circle cx="15" cy="10" r="6"/><path d="M3 26c1-6 6-9 12-9s11 3 12 9z"/><circle cx="28" cy="9" r="5.5"/><path d="M27 16c6 0 10 3 11 9h-9"/></svg>
    <svg class="menu-icon" style="left:309px" width="30" height="30" viewBox="0 0 30 30" fill="none" stroke="#8a8a8a" stroke-width="1.4" aria-label="Missions and competitions"><path d="M15 2l3.8 8 8.7 1.1-6.4 6 1.7 8.7L15 21.6l-7.8 4.2 1.7-8.7-6.4-6L11.2 10z"/></svg>
    <div class="divider" style="left:374px"></div>
    <svg class="menu-icon" style="left:405px" width="32" height="30" viewBox="0 0 32 30" fill="none" stroke="#8a8a8a" stroke-width="1.4" aria-label="Notifications"><path d="M16 2c7.7 0 14 4.7 14 10.6S23.7 23.2 16 23.2c-1.6 0-3.1-.2-4.5-.6L4 27l2.2-6.3C3.6 18.8 2 15.9 2 12.6 2 6.7 8.3 2 16 2z"/><path d="M9 10h14M9 15h10"/></svg>
  </nav>

  <nav class="nav-bar" aria-label="Navigation">
    <svg class="nav-icon" style="left:89px" width="32" height="30" viewBox="0 0 32 30" fill="none" stroke="#fff" stroke-width="1.5" aria-label="Home"><path d="M3 14L16 3l13 11"/><path d="M7 11v17h18V11"/><path d="M13 28v-8h6v8"/></svg>
    <div class="divider"></div>
    <svg class="nav-icon" style="left:345px" width="30" height="30" viewBox="0 0 30 30" fill="none" stroke="#fff" stroke-width="1.5" aria-label="Settings"><circle cx="15" cy="15" r="4.5"/><path d="M13 2h4l.7 3.5 2.6 1.1 3-2 2.8 2.8-2 3 1.1 2.6L28 13v4l-3.5.7-1.1 2.6 2 3-2.8 2.8-3-2-2.6 1.1L17 28h-4l-.7-3.5-2.6-1.1-3 2-2.8-2.8 2-3-1.1-2.6L2 17v-4l3.5-.7 1.1-2.6-2-3 2.8-2.8 3 2 2.6-1.1z"/></svg>
  </nav>

  <div class="capture-button" aria-label="Create a Glimra"><div class="dot"></div></div>
</section>

</body>
</html>
```